QWB Collection and Shipping Info Sheet

I need to convert an existing rather plain-looking MS Word doc (see attached file Fecal Sample Collection and Shipping Information V2.0.doc) into a visually appealing, professional-looking doc that reflects my current brand’s look and feel (Retail Kit Cover V1.8.pdf). At the same time, I am open to looking at improving on my brand’s look.

Target Market(s)

Horse owners, Barn Managers, Equine Veterinarians

Industry/Entity Type

Horseback Riding

Font styles to use
Sans Serif

Requirements
Must have
• Must be able to fit attached content on 2 pages (1 double signed 8x11 pdf - NOT a trifold doc). Must use Pasture Vial Labs brand standards for following colors listed:
• - lime green color: C: 75 Y: 100 or R 57 G 181 B 74 (not shown in attached file)
• - bold font is Helvetica Compressed
• - body copy (paragraphs) is Helvetica Medium
• - RGB equivalent of red is #ED1C24, which is the mix R 237, G 28, B 36
• However feel free to add other colors (e.g, golds, yellows, greys. etc.)
Nice to have
• I would like the design to be eye-catching, yet easy to read because it is a step-by-step instruction sheet. Feel free to use Icons. I have several more documents that also require updating, so I would prefer the look and feel of this doc to be transferable to other similar docs (e.g., FAQs, product descriptions, sales flyers.)
Should not have
• Do not change the written content or the order of the content. This is NOT a trifold doc.

```html
<!DOCTYPE html>
<html lang="en">
<head>
<meta charset="utf-8">
<title>QWB Collection and Shipping Info Sheet</title>
<link rel="stylesheet" href="https://fonts.googleapis.com/css2?family=Arimo:wght@400;700&family=Roboto+Condensed:wght@700&display=swap">
<style>
:root{
  --brand-red:#ed1c24;
  --ink:#2b2b2b;
  --paper:#ffffff;
  --tab-grey:#e4e4e4;
  --rule-grey:#d8d8d8;
  --backdrop:#ddd2bd;
  --link-blue:#3aa0dc;
  --photo-sky:#cfd6d8;
  --photo-coat:#8a7656;
}
*{box-sizing:border-box;margin:0;padding:0}
html,body{width:1200px;height:898px;overflow:hidden;background:var(--backdrop)}
body{font-family:"Arimo",Helvetica,Arial,sans-serif;color:var(--ink);position:relative}
.sheet{position:absolute;top:80px;width:570px;height:738px;background:var(--paper);overflow:hidden;box-shadow:0 6px 18px rgba(0,0,0,.18)}
.sheet--cover{left:20px}
.sheet--steps{left:610px}
.sheet svg.shapes{position:absolute;inset:0}
.abs{position:absolute}

/* cover */
.brand{left:400px;top:38px;display:flex;align-items:center;gap:8px}
.brand__dot{width:22px;height:22px;border-radius:50%;background:var(--brand-red)}
.brand__name{font-family:"Roboto Condensed",sans-serif;font-weight:700;font-size:17px;color:var(--brand-red);line-height:1}
.cover-title{left:40px;top:120px;font-weight:700;font-size:30px;color:var(--brand-red)}
.cover-sub{left:42px;top:160px;font-weight:700;font-size:19px;color:var(--ink)}
.horse-photo{left:40px;top:255px;width:285px;height:295px;background:linear-gradient(160deg,var(--photo-sky) 0%,#9aa58a 45%,var(--photo-coat) 75%,#3f3a2c 100%)}
.info{left:345px;width:212px;color:#fff}
.info h2{font-family:"Roboto Condensed",sans-serif;font-weight:700;font-size:17px;line-height:1;text-transform:uppercase;margin-bottom:4px}
.info p{font-size:9.2px;line-height:1.32}
.steps-head{left:345px;top:560px;width:212px;font-family:"Roboto Condensed",sans-serif;font-weight:700;font-size:15px;color:#fff;text-align:center;border-bottom:1.5px solid #fff;padding-bottom:3px}
.step{left:345px;width:215px;display:flex;gap:8px;color:#fff}
.step__icon{flex:0 0 28px;height:28px;border-radius:50%;background:#fff;display:flex;align-items:center;justify-content:center}
.step h3{font-family:"Roboto Condensed",sans-serif;font-weight:700;font-size:12px}
.step p{font-size:8.8px;line-height:1.3}
.handle{left:410px;top:722px;font-size:7px;color:#fff}
.kit{left:40px;top:565px;width:285px}
.kit h2{font-family:"Roboto Condensed",sans-serif;font-weight:700;font-size:17px;text-align:right;border-bottom:2px solid var(--brand-red);padding-bottom:2px;margin-bottom:7px}
.kit p{font-size:8.6px;font-weight:700;line-height:1.3;margin-bottom:3px}
.kit li{font-size:8.8px;line-height:1.35;list-style:none}
.kit li::before{content:"• "}
.kit .url{font-size:8.6px;text-align:center;border-bottom:2px solid var(--brand-red);padding-bottom:3px;margin-top:5px}

/* instructions */
.tab{right:0;top:0;width:170px;height:34px;background:var(--tab-grey);font-weight:700;font-size:11px;display:flex;align-items:center;justify-content:center}
.steps-title{left:26px;top:40px;font-weight:700;font-size:17px;color:var(--brand-red)}
.col{top:78px;width:250px;list-style:none}
.col--a{left:26px}.col--b{left:296px}
.col li{position:relative;padding-left:12px;font-size:7.5px;line-height:1.32;margin-bottom:9px}
.col li::before{content:"";position:absolute;left:0;top:2px;width:6px;height:6px;border-radius:50%;background:var(--brand-red)}
.alert{color:var(--brand-red)}
.link{color:var(--link-blue)}
.notice{font-family:"Roboto Condensed",sans-serif;font-weight:700;font-size:8px;color:var(--brand-red);margin:0 0 9px 12px}
.contact{right:26px;top:575px;width:190px;color:#fff;text-align:right}
.contact h2{font-size:13px;font-weight:700;border-bottom:1.5px solid #fff;padding-bottom:3px;margin-bottom:6px}
.contact p{font-size:8.4px;line-height:1.5;text-align:left}
.site{right:26px;top:712px;font-size:8.5px;color:#fff}
</style>
</head>
<body>

<section class="sheet sheet--cover">
  <svg class="shapes" width="570" height="738" viewBox="0 0 570 738">
    <polygon points="400,0 570,0 570,250 430,250" fill="var(--tab-grey)"/>
    <polygon points="335,330 570,250 570,738 0,738 0,730 335,714" fill="var(--brand-red)"/>
    <line x1="300" y1="246" x2="440" y2="208" stroke="var(--rule-grey)" stroke-width="3"/>
    <line x1="325" y1="552" x2="255" y2="568" stroke="var(--rule-grey)" stroke-width="3"/>
  </svg>
  <div class="abs brand"><span class="brand__dot"></span><span class="brand__name">PASTURE VIAL LABS</span></div>
  <div class="abs cover-title">Equine Fecal Test Kit</div>
  <div class="abs cover-sub">Parasite Egg Count Test for Horses</div>
  <div class="abs horse-photo" role="img" aria-label="Photo of a bay horse's head wearing a leather halter against green trees"></div>

  <div class="abs info" style="top:336px">
    <h2>Why<br>to test?</h2>
    <p>Protecting your horse from harmful internal parasites is a critical step in keeping your horse healthy. Internal parasites, left undetected, can hinder your horse's performance and contribute to your horse's declining health.</p>
  </div>
  <div class="abs info" style="top:446px">
    <h2>When<br>to test?</h2>
    <p>Perform two test cycles annually on your horse. One in the Spring and one in the Fall. Each cycle consists of two fecal egg count tests. One before a deworming treatment, and another test 14 days after a deworming treatment.</p>
  </div>
  <div class="abs steps-head">3 EASY STEPS</div>
  <div class="abs step" style="top:590px">
    <span class="step__icon"><svg width="16" height="16" viewBox="0 0 16 16"><line x1="10" y1="2" x2="7" y2="9" stroke="var(--brand-red)" stroke-width="2"/><path d="M4 9h6l-1 5H5z" fill="var(--brand-red)"/></svg></span>
    <div><h3>SCOOP</h3><p>Collect a fecal sample from your horse using the enclosed collection bag.</p></div>
  </div>
  <div class="abs step" style="top:633px">
    <span class="step__icon"><svg width="16" height="16" viewBox="0 0 16 16"><rect x="2" y="4" width="12" height="9" fill="none" stroke="var(--brand-red)" stroke-width="1.6"/><line x1="2" y1="7" x2="14" y2="7" stroke="var(--brand-red)" stroke-width="1.4"/></svg></span>
    <div><h3>SEAL</h3><p>Place the sample into the thermal packaging provided.</p></div>
  </div>
  <div class="abs step" style="top:676px">
    <span class="step__icon"><svg width="18" height="16" viewBox="0 0 18 16"><rect x="1" y="4" width="10" height="7" fill="none" stroke="var(--brand-red)" stroke-width="1.5"/><path d="M11 6h4l2 3v2h-6z" fill="none" stroke="var(--brand-red)" stroke-width="1.5"/><circle cx="5" cy="13" r="1.6" fill="var(--brand-red)"/><circle cx="14" cy="13" r="1.6" fill="var(--brand-red)"/></svg></span>
    <div><h3>SEND</h3><p>Ship the sample to the pre-addressed lab and receive fast, accurate results.</p></div>
  </div>
  <div class="abs handle">@pasturevialabs</div>

  <div class="abs kit">
    <h2>THE KIT</h2>
    <p>This test kit contains all the materials you need to test one horse for internal parasites:</p>
    <ul>
      <li>1 Large Fecal Collection Bag</li>
      <li>1 Gel Refrigerant Pack</li>
      <li>1 Pre-addressed Insulated Thermal Shipping Mailer</li>
      <li>1 Equine Parasite Collection Information Form</li>
      <li>1 Collection and Shipping Instruction Sheet</li>
    </ul>
    <div class="url">www.pasturevialabs.com</div>
  </div>
</section>

<section class="sheet sheet--steps">
  <svg class="shapes" width="570" height="738" viewBox="0 0 570 738">
    <polygon points="0,738 0,690 570,500 570,738" fill="var(--brand-red)"/>
  </svg>
  <div class="abs tab">Instructions</div>
  <div class="abs steps-title">How to Collect &amp; Ship a Fecal Sample</div>

  <ul class="abs col col--a">
    <li>Begin by removing the Pasture Vial Labs Kit contents from the packaging. Confirm that your Kit contains the following items:<br>1 Resealable Fecal Collection Bag<br>1 Gel Refrigerant Pack<br>1 Pre-Addressed Shipping Thermal Bubble Mailer<br>1 Equine Parasite Collection &amp; Treatment Form</li>
    <li>Complete the Equine Parasite Collection &amp; Treatment Form. A Step-by-Step Video is available at www.pasturevialabs.com/collect-sample. Fill out the form before you collect the sample. If you have any questions, call us at 555-014-2290 or email help@pasturevialabs.com</li>
    <li>Place the Gel Refrigerant Pack in the freezer at least 12 hours prior to shipping your sample. The frozen gel pack helps keep the sample cool during shipping. If your sample is warm when you collect it, place it in the refrigerator to cool for at least 30 minutes before packaging it for shipping. <span class="alert">Never freeze the fecal sample.</span></li>
    <li>Label the Fecal Collection Bag. Using a ballpoint pen or permanent marker, write your horse's name and date of collection in the blank white space provided on the outside of the Fecal Collection Bag.</li>
    <li>Positively Identify Your Horse's Manure Pile. Determine with certainty the fecal sample has come from your horse, if your horse cohabitates. If necessary, isolate your horse where you know you can collect a sample without doubt. If sending more than one sample, use one Fecal Collection Bag for each sample taken. <span class="alert">(Never combine samples from different horses in the same bag if you are collecting samples for more than one horse.)</span><br>The manure sample must be fresh. Ideally, collect the sample shortly after your horse has passed it. Parasitic matter deteriorates over time, which affects the test results. Schedule collection of samples in the morning if possible. Avoid collecting a manure sample that contains dirt, shavings, grass, etc. Select the sample from the top or middle of the manure pile. Avoid taking the sample from the portion of the pile touching the ground to minimize potential contamination.</li>
  </ul>

  <ul class="abs col col--b">
    <li>DIG IN! Once you have identified your horse's sample, turn the fecal collection bag inside out. A Step-by-Step Video is available at <span class="link">https://pasturevialabs.com/video/collection-bag</span>. With the label on the inside of the bag, place your hand inside the bag and collect the fecal nugget of choice. Ideally, the sample size should be larger than a golf ball but smaller than a tennis ball. Carefully return the bag right-side-out by using your other hand to pull the bag back over the hand grasping the sample.</li>
    <li>Remove as much air as possible and seal the Fecal Collection Bag securely. Elimination of air from the fecal collection bag helps to preserve the sample and prevents parasitic eggs from hatching. Parasite eggs are anaerobic (living in the absence of air or oxygen) and removing excess air from the bag keeps them alive longer. <span class="alert">Make certain the bag is completely sealed to avoid leakage.</span></li>
    <li>Place the sealed Fecal Collection Bag in the Pre-Addressed Shipping Thermal Bubble Mailer. If you are not able to ship your sample on the same day it is collected, simply place the Pre-Addressed Shipping Thermal Bubble Mailer with the sample in the refrigerator (&lt;39 F) until you are ready to ship it. Remember, DO NOT FREEZE the sample.</li>
    <div class="notice">ONLY USE THE PASTURE VIAL LABS PACKAGING PROVIDED. DO NOT SUBSTITUTE.</div>
    <li>Immediately prior to shipping, retrieve the Gel Refrigerant Pack from the freezer and place it inside the Pre-Addressed Shipping Thermal Bubble Mailer, next to the sealed Fecal Collection Bag. For the Lab to process your sample in a timely manner, ship the sample early in the week to ensure receipt by the Lab prior to the weekend. It is highly recommended that your sample arrive at the lab within two days of its collection. After the Lab receives your horse's fecal sample, a test will be performed to analyze and calculate your horse's parasite burden. You will receive a detailed report summarizing the type and number of eggs found in the sample. Depending on your preferences indicated on your Equine Parasite Collection &amp; Treatment Form, the results will be emailed or sent via US Postal Service.</li>
  </ul>

  <div class="abs contact">
    <h2>Any question?</h2>
    <p>Email us at help@pasturevialabs.com<br>call 555-014-2290<br>Please check<br>social.pasturevialabs.com/page<br>for store hours</p>
  </div>
  <div class="abs site">www.pasturevialabs.com</div>
</section>

</body>
</html>
```